Northgate Process Solutions

8.5 x 11 flyer one or two sides is fine. This will be used for a trade show. See message for details

Target Market(s)

Refineries and Petrochemical plants

Industry/Entity Type

Oil

```html
<!DOCTYPE html>
<html lang="en">
<head>
<meta charset="utf-8">
<title>Northgate Process Solutions – Trade Show Flyer</title>
<link rel="stylesheet" href="https://fonts.googleapis.com/css2?family=Raleway:wght@300;400;500;700;800&family=Noto+Serif:ital,wght@1,700&display=swap">
<style>
  :root {
    --green: #008753;
    --green-dark: #006b41;
    --green-light: #6fd3a6;
    --black: #000000;
    --ink: #1c1c1c;
    --white: #ffffff;
    --page-bg: #e6e6e6;
    --photo-sky: #3f7fc8;
    --photo-steel: #c7d3de;
    --photo-navy: #2b3272;
  }
  * { margin: 0; padding: 0; box-sizing: border-box; }
  html, body { width: 1200px; height: 1117px; overflow: hidden; background: var(--page-bg); }
  .stage { position: relative; width: 1200px; height: 1117px; }
  .flyer {
    position: absolute; left: 219px; top: 20px;
    width: 1170px; height: 1654px;
    transform: scale(0.6511); transform-origin: top left;
    background: var(--white);
    font-family: "Raleway", sans-serif;
    color: var(--ink);
    overflow: hidden;
  }
  .flyer-shapes { position: absolute; inset: 0; }
  .brand-name {
    position: absolute; left: 97px; top: 48px; width: 440px;
    font-weight: 800; font-size: 46px; line-height: 1.05; color: var(--ink);
  }
  .headline { position: absolute; left: 97px; top: 210px; color: var(--white); }
  .headline-strong { font-weight: 800; font-size: 64px; line-height: 64px; letter-spacing: -0.5px; }
  .headline-sub { font-weight: 400; font-size: 46px; line-height: 46px; margin-top: 10px; }
  .intro {
    position: absolute; left: 97px; top: 600px; width: 975px;
    font-size: 24px; line-height: 29px; font-weight: 500; text-align: justify;
  }
  .section-tab {
    position: absolute; left: 0; top: 791px; width: 636px; height: 79px;
    display: flex; align-items: center; justify-content: center;
    color: var(--white); font-weight: 800; font-size: 37px; padding-right: 10px;
  }
  .what-we-do {
    position: absolute; left: 97px; top: 890px; width: 445px;
    font-size: 23px; line-height: 28.2px; font-weight: 400;
  }
  .industries { position: absolute; left: 688px; top: 820px; width: 450px; color: var(--white); }
  .industries h2 { font-weight: 800; font-size: 38px; line-height: 48px; }
  .industries .rule { height: 3px; background: var(--green-dark); margin: 16px 0 16px 8px; width: 442px; }
  .industries ul { list-style: none; }
  .industries li {
    display: flex; align-items: center; gap: 18px;
    font-size: 31px; font-weight: 500; height: 51.2px; padding-left: 10px;
  }
  .industries li svg { width: 24px; height: 20px; flex: none; }
  .cta {
    position: absolute; left: 0; top: 1370px; width: 1170px; text-align: center;
    font-family: "Noto Serif", serif; font-style: italic; font-weight: 700;
    font-size: 52px; line-height: 50px; color: var(--green);
  }
  .contact {
    position: absolute; top: 1518px; height: 136px;
    display: flex; align-items: center; gap: 16px;
    color: var(--white); font-weight: 700; white-space: nowrap;
  }
  .contact-web { left: 100px; font-size: 43px; }
  .contact-phone { left: 547px; font-size: 64px; }
  .contact svg { flex: none; }
</style>
</head>
<body>
<div class="stage">
  <div class="flyer">
    <svg class="flyer-shapes" width="1170" height="1654" viewBox="0 0 1170 1654">
      <defs>
        <linearGradient id="softBack" x1="0" y1="0" x2="1" y2="1">
          <stop offset="0" stop-color="#ffffff"/>
          <stop offset="0.5" stop-color="#f1f1f1"/>
          <stop offset="1" stop-color="#e4e4e4"/>
        </linearGradient>
        <linearGradient id="frameGlow" x1="0" y1="0" x2="1" y2="0">
          <stop offset="0" stop-color="var(--green)"/>
          <stop offset="0.5" stop-color="var(--green-light)"/>
          <stop offset="1" stop-color="var(--green)"/>
        </linearGradient>
        <linearGradient id="photoTones" x1="0" y1="0" x2="0" y2="1">
          <stop offset="0" stop-color="var(--photo-sky)"/>
          <stop offset="0.45" stop-color="var(--photo-steel)"/>
          <stop offset="1" stop-color="var(--photo-navy)"/>
        </linearGradient>
      </defs>
      <rect class="soft-backdrop" x="0" y="552" width="1170" height="788" fill="url(#softBack)"/>
      <polygon class="header-band" fill="var(--black)"
        points="0,172 542,172 605,27 645,27 535,274 585,385 507,552 0,552"/>
      <polygon class="photo-frame" fill="var(--green)"
        points="650,27 1170,27 1170,552 662,552 544,274"/>
      <rect class="photo-frame-glow" x="690" y="510" width="480" height="42" fill="url(#frameGlow)"/>
      <polygon class="photo-frame-inner" fill="var(--green-dark)"
        points="690,27 1170,27 1170,510 690,510 582,274"/>
      <polygon class="hero-photo" role="img" aria-label="Photo: two refinery workers in hard hats and navy coveralls inspecting equipment among plant pipework"
        fill="url(#photoTones)" points="705,27 1170,27 1170,502 700,502 598,274"/>
      <polygon class="tab-band" fill="var(--black)" points="0,791 636,791 622,870 0,870"/>
      <polygon class="industries-panel" fill="var(--green)" points="646,791 1170,791 1170,1340 535,1340"/>
      <polygon class="footer-web" fill="var(--green)" points="0,1518 478,1518 448,1654 0,1654"/>
      <polygon class="footer-phone" fill="var(--black)" points="496,1518 1170,1518 1170,1654 466,1654"/>
    </svg>

    <div class="brand-name">Northgate Process Solutions</div>

    <div class="headline">
      <div class="headline-strong">YOUR Global<br>STRATEGIC<br>PARTNER</div>
      <div class="headline-sub">FOR PRODUCTIVE<br>SOLUTIONS</div>
    </div>

    <p class="intro">Northgate now operates on a global scale providing product services and logistics coordination throughout North America, along with major exports into multiple other countries around the world. In doing so, Northgate is now your premiere partner to source your residual materials as a feedstock into a secondary market; thereby improving your bottom line and improving the sustainability of our environment.</p>

    <div class="section-tab">WHAT WE DO</div>

    <p class="what-we-do">Northgate Process Solutions utilizes a multi-faceted approach by supporting various manufacturers, refineries, blender/ packagers and distributors by purchasing residual by-products, co-products, bottoms, off spec or out of date and surplus material. We truly pride ourselves on our ability to source your residual materials as a feedstock into a secondary market; thereby improving your bottom line and improving the sustainability of our environment. In addition, we also review waste material for reuse or recycle. Whether truck, rail or barge, Northgate is here to meet your needs.</p>

    <section class="industries">
      <h2>INDUSTRIES SERVED</h2>
      <div class="rule"></div>
      <ul>
        <li><svg viewBox="0 0 24 20"><path d="M2 10 L9 17 L22 3" fill="none" stroke="#fff" stroke-width="4"/></svg>Lubes And Grease</li>
        <li><svg viewBox="0 0 24 20"><path d="M2 10 L9 17 L22 3" fill="none" stroke="#fff" stroke-width="4"/></svg>Petrochemicals</li>
        <li><svg viewBox="0 0 24 20"><path d="M2 10 L9 17 L22 3" fill="none" stroke="#fff" stroke-width="4"/></svg>Pharmaceutical</li>
        <li><svg viewBox="0 0 24 20"><path d="M2 10 L9 17 L22 3" fill="none" stroke="#fff" stroke-width="4"/></svg>Bio Diesel</li>
        <li><svg viewBox="0 0 24 20"><path d="M2 10 L9 17 L22 3" fill="none" stroke="#fff" stroke-width="4"/></svg>Specialty</li>
        <li><svg viewBox="0 0 24 20"><path d="M2 10 L9 17 L22 3" fill="none" stroke="#fff" stroke-width="4"/></svg>Refineries &amp; Distillation</li>
        <li><svg viewBox="0 0 24 20"><path d="M2 10 L9 17 L22 3" fill="none" stroke="#fff" stroke-width="4"/></svg>Animal Feed</li>
        <li><svg viewBox="0 0 24 20"><path d="M2 10 L9 17 L22 3" fill="none" stroke="#fff" stroke-width="4"/></svg>Fuel Blending</li>
      </ul>
    </section>

    <p class="cta">Call us today to find out how we can<br>better serve your needs.</p>

    <div class="contact contact-web">
      <svg width="40" height="40" viewBox="0 0 40 40">
        <circle cx="20" cy="20" r="19" fill="#fff"/>
        <g fill="none" stroke="var(--green)" stroke-width="2">
          <circle cx="20" cy="20" r="12"/>
          <ellipse cx="20" cy="20" rx="5" ry="12"/>
          <line x1="8" y1="20" x2="32" y2="20"/>
          <line x1="10" y1="14" x2="30" y2="14"/>
          <line x1="10" y1="26" x2="30" y2="26"/>
        </g>
      </svg>
      <span>the-nps.com</span>
    </div>

    <div class="contact contact-phone">
      <svg width="50" height="50" viewBox="0 0 50 50">
        <circle cx="25" cy="25" r="24" fill="#fff"/>
        <path d="M17 13 l5 -1 l3 8 l-3 3 c2 4 5 7 9 9 l3 -3 l8 3 l-1 5 c-1 2 -3 3 -5 3 c-11 -1 -21 -11 -22 -22 c0 -2 1 -4 3 -5z" fill="var(--black)"/>
      </svg>
      <span>(555) 014-2000</span>
    </div>
  </div>
</div>
</body>
</html>
```